7 P's for Healthcare Companies - Textbook Graphic

Can you create a graphic for me for a medical textbook? The goal is to show 7 critical features of a healthcare startup and the audience is physicians with limited business backgrounds.

Please include a picture of young, male emergency physician in the middle of the graphic. Show them evaluating an idea. Can you surround the physician with bold writing for the seven components, and use brief descriptions and simple images or graphics to illustrate the point?

The image should be somewhat formal, but it's OK to be lighthearded.

The seven P's and brief descriptions include the following:
Product: what is their market solution?
(Intellectual) Property: do they have a patent or trademark?
Product Clearance: how will they get KLN approval and TPR clearance?
Payment: how will they make money?
Pilots: have they applied their product in a healthcare setting?
Physician and Patient feedback: Do doctors and patients like their product?
Publication: do they have evidence their product works?

More detail and information is available at this website: https://quvenlo.com/blog/uncategorized/healthcare-framework/

I will need to own this image

```html
<!DOCTYPE html>
<html lang="en">
<head>
<meta charset="utf-8">
<title>7 P's to evaluate healthcare companies</title>
<link rel="stylesheet" href="https://fonts.googleapis.com/css2?family=Bebas+Neue&family=Open+Sans:wght@800&family=Source+Sans+3:wght@400&display=swap">
<style>
  :root {
    --bg-top: #0b1de2;
    --bg-bottom: #17aaee;
    --brand-box: #0a14d8;
    --accent: #1a20df;
    --panel: #ffffff;
    --ink: #1b1b1b;
    --white: #ffffff;
  }
  * { margin: 0; padding: 0; box-sizing: border-box; }
  html, body { width: 1200px; height: 1195px; overflow: hidden; }
  body { background: var(--bg-bottom); }
  .canvas {
    position: relative;
    width: 1200px;
    height: 1195px;
    overflow: hidden;
    background: linear-gradient(180deg, var(--bg-top) 0%, #0d3fe6 35%, var(--bg-bottom) 100%);
    font-family: "Source Sans 3", Arial, sans-serif;
  }
  .shapes { position: absolute; inset: 0; width: 1200px; height: 1195px; }
  .brand {
    position: absolute; left: 44px; top: 24px; width: 320px; height: 153px;
    background: var(--brand-box);
    display: flex; align-items: center; gap: 14px; padding-left: 34px;
  }
  .brand-mark { width: 26px; height: 26px; background: var(--white); }
  .brand-name {
    font-family: "Open Sans", Arial, sans-serif; font-weight: 800;
    font-size: 54px; color: var(--white); letter-spacing: -1px;
  }
  .title {
    position: absolute; right: 62px; top: 40px; width: 680px;
    text-align: right; color: var(--white);
    font-family: "Open Sans", Arial, sans-serif; font-weight: 800;
    font-size: 45px; line-height: 48px; letter-spacing: -0.3px;
  }
  .physician-photo {
    position: absolute; left: 345px; top: 560px; width: 565px; height: 635px;
    border-radius: 240px 240px 0 0;
    background: linear-gradient(180deg, #d9c2ad 0%, #eef1f5 40%, #f5f7fa 100%);
  }
  .block {
    position: absolute; transform: translateX(-50%);
    text-align: center; color: var(--ink);
  }
  .heading {
    font-family: "Bebas Neue", "Arial Narrow", sans-serif;
    color: var(--accent); font-size: 52px; line-height: 46px; white-space: nowrap;
  }
  .heading.small { font-size: 40px; line-height: 33px; }
  .rule { width: 38px; height: 4px; background: var(--accent); margin: 4px auto 8px; }
  .desc { font-size: 15.5px; line-height: 16.8px; }
  .desc.large { font-size: 16.5px; line-height: 20px; }
  .icon { position: absolute; transform: translate(-50%, -50%); }
</style>
</head>
<body>
<div class="canvas">
  <svg class="shapes" viewBox="0 0 1500 1500" preserveAspectRatio="none" aria-hidden="true">
    <g fill="#ffffff">
      <polygon points="752,226 955,368 880,608 628,608 553,368"/>
      <polygon points="290,374 540,374 615,612 415,755 210,612"/>
      <polygon points="960,374 1218,374 1293,612 1090,757 890,612"/>
      <polygon points="205,625 405,770 330,1003 80,1003 5,770"/>
      <polygon points="1300,625 1500,770 1425,1003 1180,1003 1102,770"/>
      <polygon points="80,1020 330,1020 405,1255 205,1400 5,1255"/>
      <polygon points="1175,1020 1425,1020 1500,1255 1305,1400 1105,1255"/>
    </g>
  </svg>

  <div class="brand">
    <span class="brand-mark"></span>
    <span class="brand-name">quvenlo</span>
  </div>

  <h1 class="title">7 P’s to evaluate healthcare companies: A framework for physicians</h1>

  <div class="physician-photo" role="img" aria-label="Smiling young physician in a white coat with a stethoscope, reviewing an idea on a tablet"></div>

  <!-- Pilots -->
  <svg class="icon" style="left:602px;top:243px" width="80" height="60" viewBox="0 0 80 60" aria-hidden="true">
    <path d="M22 42 C30 18 52 6 76 4 C74 28 62 46 38 56 Z" fill="var(--accent)"/>
    <circle cx="54" cy="24" r="7" fill="#fff"/>
    <path d="M4 40 L20 40 M8 48 L22 48 M14 56 L26 54" stroke="var(--accent)" stroke-width="4" stroke-linecap="round"/>
  </svg>
  <div class="block" style="left:598px;top:287px;width:228px">
    <div class="heading">Pilots</div>
    <div class="rule"></div>
    <p class="desc">Healthcare startups achieve traction by obtaining early customers. The first product users from physician offices and hospitals provide feedback that can be used to improve the solution before scaling the company.</p>
  </div>

  <!-- Property -->
  <div class="block" style="left:328px;top:318px;width:226px">
    <div class="heading">Property</div>
    <div class="rule"></div>
    <p class="desc">Patents can be obtained for medical devices, pharmaceutical compounds, and digital health assets. These provide protection from knockoff products and also provide companies with a valuable asset.</p>
  </div>
  <svg class="icon" style="left:328px;top:530px" width="104" height="48" viewBox="0 0 104 48" aria-hidden="true">
    <g fill="var(--accent)" transform="rotate(-14 52 24)">
      <rect x="4" y="22" width="22" height="4"/>
      <rect x="24" y="16" width="54" height="16" rx="3"/>
      <rect x="32" y="8" width="6" height="10"/><rect x="46" y="8" width="6" height="10"/><rect x="60" y="8" width="6" height="10"/>
      <rect x="78" y="21" width="14" height="6"/>
      <rect x="92" y="12" width="5" height="24"/>
    </g>
  </svg>

  <!-- Payment -->
  <div class="block" style="left:874px;top:318px;width:250px">
    <div class="heading">Payment</div>
    <div class="rule"></div>
    <p class="desc">This ‘P’ recognizes the cost of the product and how a company is reimbursed. This includes the company cost to product the product.</p>
  </div>
  <svg class="icon" style="left:866px;top:515px" width="52" height="66" viewBox="0 0 52 66" aria-hidden="true">
    <rect x="2" y="2" width="42" height="62" rx="5" fill="var(--accent)"/>
    <path d="M17 10 v12 M11 16 h12" stroke="#fff" stroke-width="4"/>
    <path d="M10 32 h24 M10 40 h20 M10 48 h24" stroke="#fff" stroke-width="3"/>
    <circle cx="40" cy="42" r="10" fill="#fff"/>
    <text x="40" y="48" text-anchor="middle" font-size="17" font-weight="700" fill="var(--accent)" font-family="Arial, sans-serif">$</text>
  </svg>

  <!-- Process -->
  <svg class="icon" style="left:162px;top:566px" width="72" height="72" viewBox="0 0 72 72" aria-hidden="true">
    <circle cx="36" cy="36" r="26" fill="none" stroke="var(--accent)" stroke-width="7" stroke-dasharray="30 11"/>
    <path d="M30 24 h12 v6 h6 v12 h-6 v6 h-12 v-6 h-6 v-12 h6 z" fill="var(--accent)"/>
  </svg>
  <div class="block" style="left:162px;top:606px;width:212px">
    <div class="heading">Process</div>
    <div class="rule"></div>
    <p class="desc">While not every health innovation requires KLN clearance, understanding how a product you’re evaluating is regulated is important for assuring patient safety and mitigating potential risk.</p>
  </div>

  <!-- Publications -->
  <svg class="icon" style="left:1046px;top:564px" width="66" height="64" viewBox="0 0 66 64" aria-hidden="true">
    <rect x="2" y="4" width="46" height="56" rx="3" fill="var(--accent)"/>
    <path d="M10 16 h26 M10 26 h22 M10 36 h18" stroke="#fff" stroke-width="3"/>
    <path d="M34 44 L58 6 L64 10 L40 48 L32 52 Z" fill="var(--accent)" stroke="#fff" stroke-width="2"/>
  </svg>
  <div class="block" style="left:1046px;top:612px;width:232px">
    <div class="heading">Publications</div>
    <div class="rule"></div>
    <p class="desc">Particularly for diagnostics, medical devices, and drugs, track the efficacy of treatment. Sometimes this is internal information, but companies will publish studies related to their product’s performance.</p>
  </div>

  <!-- Product -->
  <svg class="icon" style="left:162px;top:853px" width="66" height="66" viewBox="0 0 66 66" aria-hidden="true">
    <path d="M4 6 L30 2 L56 6 V30 C56 48 42 58 30 64 C18 58 4 48 4 30 Z" fill="var(--accent)"/>
    <path d="M30 6 V58" stroke="#fff" stroke-width="3"/>
    <path d="M38 22 V40 C38 50 56 50 56 40 V34" fill="none" stroke="#fff" stroke-width="6"/>
    <path d="M38 22 V40 C38 50 56 50 56 40 V34" fill="none" stroke="var(--accent)" stroke-width="3"/>
    <circle cx="56" cy="30" r="6" fill="var(--accent)" stroke="#fff" stroke-width="2"/>
  </svg>
  <div class="block" style="left:162px;top:903px;width:256px">
    <div class="heading">Product</div>
    <div class="rule"></div>
    <p class="desc large">The first step is to evaluate the proposed solution and how well it addresses a medical practice pain point. prototype.</p>
  </div>

  <!-- Physician/Patient Feedback -->
  <svg class="icon" style="left:1042px;top:849px" width="64" height="58" viewBox="0 0 64 58" aria-hidden="true">
    <path d="M2 8 h48 v36 h-30 l-10 10 v-10 h-8 z" fill="var(--accent)"/>
    <path d="M10 18 h20 M10 26 h28 M10 34 h24" stroke="#fff" stroke-width="3"/>
    <path d="M36 30 L58 4 L63 8 L41 34 L34 36 Z" fill="var(--accent)" stroke="#fff" stroke-width="2"/>
  </svg>
  <div class="block" style="left:1048px;top:889px;width:256px">
    <div class="heading small">Physician/Patient<br>Feedback</div>
    <div class="rule"></div>
    <p class="desc">It’s important to evaluate what kind of feedback was sought from patients and physicians as the product was developed.</p>
  </div>
</div>
</body>
</html>
```